Name card design for KOV mobile accessories company

KOV is an upmarket brand, we are looking for professional business card design.

the design should be neat and simple but giving a strong feeling.
should not be colorful. make it black/white/gray tone

Name:
Job title:
Contact no.:
company address: i would like the company address to be very small and thin.
link to social media profile:
company website:

*the company have no website yet
as the project is done please i also would like the font that use in design as well; for more further people in company need a business card:)
Updates

Thank you for all super fast submission :D they're all look cool!

i have just update my brief to make the statement clearer, please check it out :)
if you have any question please dont hesitate to ask.
i would like see more design from you! 
Keep it up!  :D

Target Market(s)

Company target are upmarket company distributor, such as Vordane and Pilto store.

Industry/Entity Type

Business

Font styles to use
Serif
Sans Serif
Other font styles liked:
• Formal and mordern

Colors
ffffff
eeeeee
d3d3d3
919191
474747
1b1b1b
000000
333333

Requirements
Must have
• The design must be professional clean and clear but also Strong and Modern!
text should be formal and mordern
Should not have
• No complicated design!

```html
<!DOCTYPE html>
<html lang="en">
<head>
<meta charset="utf-8">
<title>KOV Business Card</title>
<link rel="stylesheet" href="https://fonts.googleapis.com/css2?family=Montserrat:wght@300;400;600;700&display=swap">
<style>
  :root {
    --backdrop: #e6e9e9;
    --card: #5b5b5b;
    --card-edge: #4f4f4f;
    --ink-foil: #d3d3d3;
    --ink-foil-soft: #b9b9b9;
    --ink-deboss: #3a3a3a;
    --rule: #2f2f2f;
  }
  * { margin: 0; padding: 0; box-sizing: border-box; }
  html, body {
    width: 1200px;
    height: 799px;
    overflow: hidden;
    background: var(--backdrop);
  }
  .canvas {
    position: relative;
    width: 1200px;
    height: 799px;
    display: flex;
    align-items: center;
    justify-content: center;
  }
  .business-card {
    position: relative;
    width: 900px;
    height: 550px;
    background: var(--card);
    border: 1px solid var(--card-edge);
    box-shadow: 0 10px 30px rgba(0, 0, 0, 0.18);
    font-family: "Montserrat", sans-serif;
    color: var(--ink-foil);
  }
  .company-address {
    position: absolute;
    left: 64px;
    top: 250px;
    font-weight: 300;
    font-size: 21px;
    line-height: 38px;
    letter-spacing: 3px;
    color: var(--ink-foil-soft);
    font-style: normal;
  }
  .divider {
    position: absolute;
    left: 432px;
    top: 130px;
    width: 2px;
    height: 320px;
    background: var(--rule);
  }
  .identity {
    position: absolute;
    left: 470px;
    top: 138px;
    width: 370px;
  }
  .identity .person-name {
    font-weight: 300;
    font-size: 27px;
    letter-spacing: 3px;
    color: var(--ink-deboss);
  }
  .identity .job-title {
    margin-top: 4px;
    text-align: right;
    font-weight: 700;
    font-size: 24px;
    letter-spacing: 4px;
    color: var(--ink-foil-soft);
  }
  .contact-list {
    position: absolute;
    right: 60px;
    top: 300px;
    list-style: none;
    text-align: right;
    font-size: 22px;
    line-height: 40px;
    letter-spacing: 3px;
  }
  .contact-list .mobile { font-weight: 400; }
  .contact-list .mobile .label { font-weight: 300; color: var(--ink-deboss); }
  .contact-list .phone { font-weight: 700; }
  .contact-list .web,
  .contact-list .email { font-weight: 600; font-size: 20px; }
</style>
</head>
<body>
  <main class="canvas">
    <section class="business-card" aria-label="KOV business card">
      <address class="company-address">
        KOV pty. ltd.<br>
        41 Wrenfield street<br>
        3185 Linmere<br>
        VIC Aus.
      </address>

      <div class="divider" aria-hidden="true"></div>

      <header class="identity">
        <p class="person-name">Marcus T. Halden</p>
        <p class="job-title">DIRECTOR</p>
      </header>

      <ul class="contact-list">
        <li class="mobile"><span class="label">m:</span> 888 714 206</li>
        <li class="phone">p: 8555 9170</li>
        <li class="web">www.kovline.com</li>
        <li class="email">email@kovline.com</li>
      </ul>
    </section>
  </main>
</body>
</html>
```